Flyer für einen Hersteller von Campingzubehör
Zielgruppe
Wir sind Hersteller von Campingzubehör, in der Hauptsache für Wohnmobile und Markisen. Zielgruppe sind daher alle Camper mit entsprechenden Freizeitfahrzeugen. Bei diesem Flyer soll der Camper aufmerksam werden, das der Sonnenschutz individuell bedruckt werden kann, mit eigenen Motiven. Viele lasse sich auf das Sonnensegel eine schöne Urlaubserinnerung, den Hund, oder etwas was dem Camper lieb und wichtig ist. Eben ganz individuell. Wichtig ist das der Sonnenschutz Made in Germany ist! und absolut werkzeugfrei handzuhaben ist. Spezifikationen werden von uns eingefügt.
Aufgabenstellung
Der Flyer soll nach der beiliegenden Druckvorlage erstellt werden. Falzflyer, DIN A5, 4 Seiten. Sinngemäße Angabe in der Vorlage. Auf der 4 Seite soll das Bestellformular erscheinen, also diese Seite bitte freilassen und 'nur' die 3 Seiten gestalten.
Auf der Titelseite soll das auf das 'Schattenproblem' aufmerksam gemacht werden. Ich bin sehr gespannt! Bei Fragen bitte melden. Für den Hintergrund lasse ich dem Designer feien lauf...

```html
<!DOCTYPE html>
<html lang="de">
<head>
<meta charset="utf-8">
<title>Flyer – Individuell bedruckbare Sunblocker</title>
<link rel="stylesheet" href="https://fonts.googleapis.com/css2?family=Open+Sans:wght@400;600;700&display=swap">
<style>
  :root {
    --leaf: #8cc63f;
    --lime: #e6ef00;
    --ink: #1a1a1a;
    --paper: #ffffff;
    --sky: #bfe3ee;
    --meadow: #5fa62a;
    --grass-deep: #3f7f1c;
  }
  html, body {
    margin: 0;
    padding: 0;
    width: 741px;
    height: 1200px;
    overflow: hidden;
    background: var(--paper);
    font-family: "Open Sans", sans-serif;
  }
  .canvas {
    position: relative;
    width: 741px;
    height: 1200px;
  }
  .spread {
    position: absolute;
    display: block;
    filter: drop-shadow(0 6px 10px rgba(0,0,0,0.35));
  }
  .spread--outside { left: 68px; top: 113px; width: 609px; height: 433px; }
  .spread--inside  { left: 74px; top: 637px; width: 609px; height: 435px; }
  .t-white-fill { fill: var(--paper); }
  .t-leaf { fill: var(--leaf); }
  .t-lime { fill: var(--lime); }
  .t-ink { fill: var(--ink); }
  .brand-name { font-weight: 700; fill: var(--leaf); }
</style>
</head>
<body>
<div class="canvas">

  <!-- Outside spread: back page + title page -->
  <svg class="spread spread--outside" viewBox="0 0 1234 877" xmlns="http://www.w3.org/2000/svg">
    <defs>
      <linearGradient id="meadowScene" x1="0" y1="0" x2="0" y2="1">
        <stop offset="0" stop-color="var(--sky)"/>
        <stop offset="0.12" stop-color="#9fc98a"/>
        <stop offset="0.2" stop-color="#4f8a2a"/>
        <stop offset="0.28" stop-color="#b6d83a"/>
        <stop offset="0.55" stop-color="var(--meadow)"/>
        <stop offset="1" stop-color="var(--grass-deep)"/>
      </linearGradient>
      <linearGradient id="dogSail" x1="0" y1="0" x2="1" y2="1">
        <stop offset="0" stop-color="#6f9a3c"/>
        <stop offset="0.5" stop-color="#a0683a"/>
        <stop offset="1" stop-color="#9fbf6a"/>
      </linearGradient>
    </defs>
    <rect width="1234" height="877" fill="url(#meadowScene)" role="img" aria-label="Foto: Wohnmobile mit Markisen auf einer Wiese vor Bäumen"/>
    <rect x="196" y="130" width="352" height="225" fill="#2b2b2b" role="img" aria-label="Foto: dunkles, unbedrucktes Sonnensegel an der Markise"/>
    <rect x="691" y="132" width="332" height="220" fill="url(#dogSail)" role="img" aria-label="Foto: Sonnensegel mit Hundemotiv an der Markise"/>

    <!-- back page curve -->
    <path class="t-lime" d="M0,395 Q470,300 617,877 L0,877 Z"/>
    <path class="t-white-fill" d="M0,428 Q440,340 608,877 L0,877 Z"/>
    <!-- title page curve -->
    <path class="t-lime" d="M612,877 Q760,300 1234,395 L1234,877 Z"/>
    <path class="t-leaf" d="M624,877 Q770,330 1234,428 L1234,877 Z"/>
    <path class="t-white-fill" d="M965,877 Q960,560 1234,520 L1234,877 Z"/>

    <!-- back page -->
    <text class="t-ink" x="105" y="508" font-size="18">MADE IN</text>
    <text class="t-ink" x="103" y="532" font-size="26" font-weight="700">GERMANY</text>
    <text class="t-leaf" x="105" y="584" font-size="15" font-weight="700">KONTAKT INFORMATION</text>
    <text class="t-ink" font-size="16">
      <tspan x="105" y="605">Grünzelt Ausstattung UG</tspan>
      <tspan x="105" y="626">Wiesenweg 12</tspan>
      <tspan x="105" y="647">94500 Waldbrunn</tspan>
    </text>
    <text class="t-ink" x="103" y="692" font-size="17">motiv@gruenzelt-ausstattung.de</text>
    <text class="brand-name" x="100" y="770" font-size="40">Grünzelt</text>

    <!-- title page -->
    <text class="t-lime" x="940" y="562" font-size="70" font-weight="700" text-anchor="middle">NEU</text>
    <text class="t-ink" font-size="31">
      <tspan x="752" y="627">INDIVIDUELL</tspan>
      <tspan x="752" y="670">BEDRUCKBARE</tspan>
      <tspan x="752" y="712">SUNBLOCKER</tspan>
    </text>
    <text class="t-ink" font-size="18">
      <tspan x="754" y="754">Für den schönsten</tspan>
      <tspan x="754" y="777">schatten der Welt</tspan>
    </text>
    <text class="brand-name" x="1008" y="772" font-size="36">Grünzelt</text>
  </svg>

  <!-- Inside spread -->
  <svg class="spread spread--inside" viewBox="0 0 1232 880" xmlns="http://www.w3.org/2000/svg">
    <defs>
      <linearGradient id="meadowSceneInside" x1="0" y1="0" x2="0" y2="1">
        <stop offset="0" stop-color="var(--sky)"/>
        <stop offset="0.2" stop-color="#7fa85a"/>
        <stop offset="0.42" stop-color="#b6d83a"/>
        <stop offset="1" stop-color="var(--meadow)"/>
      </linearGradient>
      <linearGradient id="roadSail" x1="0" y1="0" x2="0" y2="1">
        <stop offset="0" stop-color="#3f86d6"/>
        <stop offset="0.45" stop-color="#cfe2f2"/>
        <stop offset="0.62" stop-color="#7b8f4a"/>
        <stop offset="1" stop-color="#b9a25e"/>
      </linearGradient>
      <linearGradient id="sunsetSail" x1="0" y1="0" x2="0" y2="1">
        <stop offset="0" stop-color="#3d5a80"/>
        <stop offset="0.45" stop-color="#c46a2a"/>
        <stop offset="0.7" stop-color="#f0a020"/>
        <stop offset="1" stop-color="#2a1a10"/>
      </linearGradient>
    </defs>
    <rect class="t-white-fill" width="1232" height="880"/>

    <rect x="0" y="0" width="613" height="450" fill="url(#meadowSceneInside)" role="img" aria-label="Foto: Wohnmobil mit Markise auf einer Wiese"/>
    <rect x="78" y="130" width="322" height="220" fill="url(#roadSail)" role="img" aria-label="Foto: Sonnensegel bedruckt mit Landstraße und Wolkenhimmel"/>

    <rect x="614" y="450" width="618" height="430" fill="url(#meadowSceneInside)" role="img" aria-label="Foto: Wohnmobil mit Markise auf einer Wiese"/>
    <rect x="695" y="580" width="318" height="220" fill="url(#sunsetSail)" role="img" aria-label="Foto: Sonnensegel bedruckt mit Sonnenuntergang am See"/>

    <!-- idea panel curve -->
    <path class="t-lime" d="M616,450 Q700,30 1232,18 L1232,450 Z"/>
    <path class="t-leaf" d="M632,450 Q720,50 1232,38 L1232,450 Z"/>
    <path class="t-white-fill" d="M958,450 Q980,150 1232,135 L1232,450 Z"/>

    <text class="t-ink" font-size="30">
      <tspan x="825" y="178">FÜR</tspan>
      <tspan x="825" y="220">EINZIGARTIGE</tspan>
      <tspan x="825" y="260">IDEEN</tspan>
    </text>
    <g class="t-lime">
      <circle cx="750" cy="284" r="5"/>
      <circle cx="750" cy="308" r="5"/>
      <circle cx="750" cy="332" r="5"/>
      <circle cx="750" cy="356" r="5"/>
      <circle cx="750" cy="380" r="5"/>
      <circle cx="750" cy="404" r="5"/>
    </g>
    <text class="t-ink" font-size="18">
      <tspan x="765" y="290">Sonnenschutz</tspan>
      <tspan x="765" y="314">Regenschutz</tspan>
      <tspan x="765" y="338">280gqm</tspan>
      <tspan x="765" y="362">Sichtschutz</tspan>
      <tspan x="765" y="386">UV Beständig</tspan>
      <tspan x="765" y="410">mit Ösen</tspan>
    </text>
    <text class="brand-name" x="1008" y="400" font-size="36">Grünzelt</text>

    <!-- description -->
    <text class="t-leaf" x="70" y="556" font-size="17">SUNBLOCKER - SICHTSCHUTZ- WETTERSCHUTZ</text>
    <text class="t-ink" font-size="14">
      <tspan x="70" y="600">Transparentes Meshewebe, das Licht und Luft durchlässt, aber Wärme</tspan>
      <tspan x="70" y="619">blockiert. Passt in jede Kederleiste von Nordhalt, Sonnora oder Flammia!</tspan>
      <tspan x="70" y="638">Das Meshgewebe ist Wasserfest und hält bis zu 96% der UV Strahlung</tspan>
      <tspan x="70" y="657">ab. Nässe ist kein Problem, das Sonnensegel wird kurz geschüttelt und</tspan>
      <tspan x="70" y="676">ist sofort trocken! Ein Stück mehr Privatsphäre am Campingplatz.</tspan>
      <tspan x="70" y="695">Das Sonnensegel wird einfach in die vorhandene Kederleiste von der</tspan>
      <tspan x="70" y="714">Markise einziehen und den Schatten genießen. Mit Ösen und dem</tspan>
      <tspan x="70" y="733">beiliegenden Befestigungsmaterial, kann das Sonnensegel schnell und</tspan>
      <tspan x="70" y="752">einfach abgespannt werden.</tspan>
      <tspan x="70" y="771">Tasche und Befestigungszubehör ist selbstständlich auch dabei.</tspan>
    </text>
  </svg>

</div>
</body>
</html>
```